Book Cover Design - Business/Self-Help Book

Book cover design for a business/self-help book. The title of the book is "OTTER Compass - Seven Quiet Habits of Steady Growth" It should also have "Unlock the Nine Hidden Keys Behind Lasting Momentum" as a subtitle somewhere.

Please see the website for an idea of the logo and sub-words: http://www.ottercompassbook.com

Book size will be 8.5" x 5.25"
Author info: Marlo Quindt

If your design includes a shark on the cover, it MUST be a hammerhead shark. Logo is attached.

I would like to stick with a red or orange theme like on the website but am open to any color idea. I like brighter colors and want the book to stand out and be attractive. If it's white, the wording and logo should be a bright color.

The back cover will just be preview text and selling points. It could have a picture in the background but will not have any pictures of the author.

If you include a spine design, please put the hammerhead logo on the spine.

Target Market(s)

Young Entrepreneurs and Business Professionals

Industry/Entity Type

Business

Requirements
Must have
• The hammerhead shark logo
Nice to have
• Look at the website - http://www.ottercompassbook.com
• It would be nice to have the six words throughout the cover similar to how it shows on the website cover picture.
Should not have
• Even though it caters to a younger crowd, it should not be cartoonish or child-like. Want a more serious and modern feel. Not too cluttered, i want the title to stand out and the shark to stand out.

```html
<!DOCTYPE html>
<html lang="en">
<head>
<meta charset="utf-8">
<title>OTTER Compass — Book Cover</title>
<link href="https://fonts.googleapis.com/css2?family=Montserrat:wght@500;600&family=Sacramento&family=Josefin+Sans:wght@400&family=Oswald:wght@600&display=swap" rel="stylesheet">
<style>
  :root {
    --stage-top: #f7941d;
    --stage-bottom: #f2570f;
    --paper: #ffffff;
    --ink: #2a1a10;
    --gold: #f6b420;
    --tagline: #ffd21a;
    --glow: #fff6cf;
    --amber: #f3a21a;
    --ember: #b55a0c;
    --umber: #5a2a08;
    --band-top: #ffbd2e;
    --band-bottom: #f4a41a;
  }
  * { margin: 0; padding: 0; box-sizing: border-box; }
  html, body { width: 888px; height: 1200px; overflow: hidden; }
  body {
    background: linear-gradient(180deg, var(--stage-top), var(--stage-bottom));
    position: relative;
  }
  .book {
    position: absolute;
    left: 73px; top: 40px;
    width: 742px; height: 1120px;
    display: flex;
    box-shadow: 0 18px 40px rgba(90, 30, 0, 0.35);
  }
  .spine {
    position: relative;
    width: 50px; height: 100%;
    background: var(--paper);
    border-right: 1px solid rgba(42, 26, 16, 0.12);
    overflow: hidden;
  }
  .spine-text {
    position: absolute;
    left: 50%; top: 40px;
    transform: translateX(-50%) rotate(180deg);
    writing-mode: vertical-rl;
    font-family: "Montserrat", sans-serif;
    font-weight: 600;
    font-size: 24px;
    letter-spacing: 3px;
    color: var(--ink);
    white-space: nowrap;
  }
  .spine-title { top: 40px; }
  .spine-author { top: 470px; font-weight: 500; font-size: 22px; }
  .spine-band {
    position: absolute;
    left: 0; bottom: 0;
    width: 100%; height: 120px;
    background: linear-gradient(180deg, var(--band-top), var(--band-bottom));
    display: flex; flex-direction: column; align-items: center; justify-content: center;
    gap: 6px;
  }
  .spine-mark {
    width: 12px; height: 12px;
    border-radius: 50%;
    background: var(--ink);
  }
  .spine-brand {
    writing-mode: vertical-rl;
    transform: rotate(180deg);
    font-family: "Montserrat", sans-serif;
    font-weight: 600;
    font-size: 13px;
    letter-spacing: 1px;
    color: var(--ink);
  }
  .cover {
    position: relative;
    width: 692px; height: 100%;
    background: var(--paper);
    overflow: hidden;
  }
  .cover-photo {
    position: absolute;
    left: 0; top: 300px;
    width: 692px; height: 710px;
    background:
      radial-gradient(circle at 28% 82%, var(--paper) 0, var(--glow) 9%, rgba(255,220,120,0.7) 22%, rgba(255,220,120,0) 45%),
      radial-gradient(ellipse at 85% 60%, var(--umber) 0, var(--ember) 35%, rgba(181,90,12,0) 70%),
      linear-gradient(180deg, var(--paper) 0%, rgba(255,255,255,0.85) 25%, var(--amber) 70%, var(--ember) 100%);
  }
  .title-main {
    position: absolute;
    top: 36px; left: 0; width: 100%;
    text-align: center;
    font-family: "Montserrat", sans-serif;
    font-weight: 600;
    font-size: 176px;
    line-height: 1;
    letter-spacing: -4px;
    color: var(--ink);
  }
  .title-script {
    position: absolute;
    top: 185px; left: 0; width: 100%;
    text-align: center;
    font-family: "Sacramento", cursive;
    font-size: 170px;
    line-height: 1;
    color: var(--gold);
  }
  .subtitle {
    position: absolute;
    top: 432px; left: 0; width: 100%;
    text-align: center;
    font-family: "Josefin Sans", sans-serif;
    font-variant: small-caps;
    font-size: 32px;
    color: var(--ink);
  }
  .tagline {
    position: absolute;
    right: 24px; top: 780px;
    width: 330px;
    text-align: right;
    font-family: "Oswald", sans-serif;
    font-weight: 600;
    font-size: 42px;
    line-height: 1.12;
    text-transform: uppercase;
    color: var(--tagline);
    transform: scaleX(0.86);
    transform-origin: right top;
  }
  .author-band {
    position: absolute;
    left: 0; bottom: 0;
    width: 100%; height: 120px;
    background: linear-gradient(180deg, var(--band-top), var(--band-bottom));
    display: flex; align-items: center; justify-content: center;
  }
  .author-name {
    font-family: "Montserrat", sans-serif;
    font-weight: 500;
    font-size: 70px;
    letter-spacing: -1px;
    color: var(--ink);
  }
</style>
</head>
<body>
  <div class="book">
    <aside class="spine">
      <span class="spine-text spine-title">OTTER COMPASS</span>
      <span class="spine-text spine-author">MARLO QUINDT</span>
      <div class="spine-band">
        <span class="spine-mark"></span>
        <span class="spine-brand">OTTER</span>
      </div>
    </aside>
    <main class="cover">
      <div class="cover-photo" role="img" aria-label="Photograph of a person silhouetted against a bright sunset, arms raised, with autumn leaves falling around"></div>
      <h1 class="title-main">OTTER</h1>
      <div class="title-script">Compass</div>
      <p class="subtitle">Seven Quiet Habits of Steady Growth</p>
      <p class="tagline">Unlock the Nine Hidden Keys Behind Lasting Momentum</p>
      <footer class="author-band">
        <span class="author-name">MARLO QUINDT</span>
      </footer>
    </main>
  </div>
</body>
</html>
```